Sleep/Snoring Business - Requires Website - Australia

We are seeking a simple to maintain website for our sleep business. The health care business provides diagnostic and treatment solutions for snoring, sleep disorders and other respiratory problems.

Ideally, colours to match the company logo (attached).

The page must be built using WORDPRESS.

Ideally site will have a home page outlining the business, with 5 sub pages - being "Diagnosis" "Treatment Options", "Prodcuts", "About Us", "Contact Us"

The site home page should include a large picture on the home page.

The "Treatment Options" and "Diagnosis" pages must include:
Allow for a few pictures with assocaited text, plus space for some embeded youtube videos.

"Prodcuts" page should have the ability to show 3-4 products across the page with text below.. that can include external URL to products

The "About Us" page must include:
1. a Map (google map) to identify the various locations. There are 6 in total.
2. A Section to describe our doctors/staff - allow for a picture and some text

The "Contact Us" page must include:
email form
telephone details

The overall design should have a clean and medical/safe feeling

Target Market(s)

People who snore and those with sleeping and respiratory disorders

Industry/Entity Type

Health Care

Coding

Coded - Design and coding required

Number of Pages Required

5+ page

Colors

Designer to choose colors to be used in the design.

Requirements
Must have
• The page must be built using WORDPRESS.
• Ideally site will have a home page outlining the business, with 5 sub pages - being "Diagnosis" "Treatment Options", "Prodcuts", "About Us", "Contact Us"
• The site home page should include a large picture on the home page.
• The "Treatment Options" and "Diagnosis" pages must include:
• Allow for a few pictures with assocaited text, plus space for some embeded youtube videos.
• "Prodcuts" page should have the ability to show 3-4 products across the page with text below.. that can include external URL to products
• The "About Us" page must include:
• 1. a Map (google map) to identify the various locations. There are 6 in total.
• 2. A Section to describe our doctors/staff - allow for a picture and some text
• The "Contact Us" page must include:
• email form
• telephone details
• Pictures must be licenced or free to use
Nice to have
• Home page pictures showing people sleeping well, snoring or fresh air (landscape) type transition pictures (at least 3).
Should not have
• Not to look cheap
• This is a high end healthcare business, so must look that way

```html
<!DOCTYPE html>
<html lang="en">
<head>
<meta charset="utf-8">
<title>Restwell Australia</title>
<link href="https://fonts.googleapis.com/css2?family=Lato:wght@400;700&display=swap" rel="stylesheet">
<style>
:root{
  --navy:#0f4a80;
  --sky:#8eb0da;
  --ink:#333333;
  --paper:#f1eff0;
  --white:#ffffff;
  --rule:#cfcfcf;
  --hero-top:#7fd9c0;
  --hero-mid:#3f9a2c;
  --hero-low:#2f7a1e;
}
*{margin:0;padding:0;box-sizing:border-box}
html,body{width:1200px;height:822px;overflow:hidden}
body{font-family:"Lato",sans-serif;color:var(--ink);background:var(--paper);position:relative}
.topbar{position:absolute;left:0;top:0;width:1200px;height:44px;background:var(--navy);color:var(--white)}
.topbar-item{position:absolute;top:0;height:44px;display:flex;align-items:center;gap:12px;padding-left:18px;border-left:1px solid rgba(255,255,255,.35)}
.topbar-phone{left:702px;width:180px;font-size:19px;font-weight:700}
.topbar-email{left:882px;width:237px;font-size:16px;border-right:1px solid rgba(255,255,255,.35)}
.site-header{position:absolute;left:0;top:44px;width:1200px;height:111px;background:var(--white)}
.brand{position:absolute;left:80px;top:34px;font-size:46px;font-weight:700;color:var(--navy);letter-spacing:-1px}
.main-nav{position:absolute;right:80px;top:44px;display:flex;gap:56px;font-size:18px}
.main-nav a{color:var(--ink);text-decoration:none;padding-bottom:6px}
.main-nav a.is-active{color:var(--navy);font-weight:700;border-bottom:2px solid var(--navy)}
.hero{position:absolute;left:0;top:155px;width:1200px;height:525px;
  background:linear-gradient(180deg,var(--hero-top) 0%,#4a8f4a 18%,var(--hero-mid) 38%,var(--hero-low) 100%)}
.hero-text{position:absolute;left:0;top:298px;width:1200px;text-align:center;color:var(--white);font-size:34px;line-height:46px;font-weight:400;text-shadow:0 1px 3px rgba(0,0,0,.35)}
.hero-text strong{font-weight:700}
.wave{position:absolute;left:0;top:540px;width:1200px;height:140px}
.dots{position:absolute;top:577px;left:0;width:1200px;display:flex;justify-content:center;gap:22px;align-items:center}
.dot{width:8px;height:8px;border-radius:50%;background:#9aa3a0}
.dot.is-current{width:14px;height:14px;background:var(--white)}
.contact-col{position:absolute;top:683px}
.contact-col h3{font-size:16px;font-weight:700;color:var(--navy);display:flex;align-items:center;gap:12px;height:20px}
.contact-col p{font-size:15px;line-height:19px;margin-top:6px}
.col-location{left:80px}.col-location p{padding-left:30px}
.col-phone{left:398px}.col-phone p{padding-left:28px}
.col-email{left:563px}.col-email p{padding-left:27px}
.col-follow{left:786px}
.social{display:flex;gap:0;margin-top:10px;padding-left:28px}
.social span{width:10px;height:10px;border-radius:50%;background:var(--ink);margin:0 12px}
.social span+span{border-left:none}
.footer-brand{position:absolute;left:972px;top:672px;font-size:40px;font-weight:700;color:var(--navy);letter-spacing:-1px}
.footer-rule{position:absolute;left:80px;top:773px;width:1040px;height:1px;background:var(--rule)}
.copyright{position:absolute;left:0;top:788px;width:1200px;text-align:center;font-size:13px}
.bottom-line{position:absolute;left:0;top:820px;width:1200px;height:2px;background:var(--navy)}
</style>
</head>
<body>
<div class="topbar">
  <div class="topbar-item topbar-phone">
    <svg width="18" height="18" viewBox="0 0 24 24"><path fill="#fff" d="M6.6 10.8a15 15 0 0 0 6.6 6.6l2.2-2.2c.3-.3.7-.4 1-.2 1.1.4 2.3.6 3.6.6.6 0 1 .4 1 1V20c0 .6-.4 1-1 1A17 17 0 0 1 3 4c0-.6.4-1 1-1h3.5c.6 0 1 .4 1 1 0 1.3.2 2.5.6 3.6.1.3 0 .7-.2 1z"/></svg>
    123-555-0190
  </div>
  <div class="topbar-item topbar-email">
    <svg width="20" height="14" viewBox="0 0 20 14"><rect x="0" y="0" width="20" height="14" fill="#fff"/><path d="M0 0 L10 8 L20 0" fill="none" stroke="#0f4a80" stroke-width="1.6"/></svg>
    info@restwellclinic.com
  </div>
</div>

<header class="site-header">
  <div class="brand">Restwell</div>
  <nav class="main-nav">
    <a class="is-active" href="#">Home</a>
    <a href="#">Diagnosis</a>
    <a href="#">Treatment</a>
    <a href="#">Products</a>
    <a href="#">About Us</a>
    <a href="#">Contact Us</a>
  </nav>
</header>

<section class="hero" role="img" aria-label="Sunlit green meadow with grazing kangaroos and a line of trees under a pale sky">
  <p class="hero-text">We provide diagnostic and treatment solutions for <strong>snoring, sleep</strong><br><strong>disorders</strong> and other <strong>respiratory problems.</strong></p>
</section>

<svg class="wave" viewBox="0 0 1200 140" preserveAspectRatio="none">
  <path d="M0,22 Q560,84 1200,33 V140 H0Z" fill="#0f4a80"/>
  <path d="M0,62 Q600,130 1200,42 V140 H0Z" fill="#8eb0da"/>
  <path d="M0,66 L44,73 Q600,150 1200,78 V140 H0Z" fill="#f1eff0"/>
</svg>
<div class="dots"><span class="dot"></span><span class="dot is-current"></span><span class="dot"></span></div>

<div class="contact-col col-location">
  <h3><svg width="16" height="20" viewBox="0 0 16 20"><path fill="#0f4a80" d="M8 0a7 7 0 0 0-7 7c0 5 7 13 7 13s7-8 7-13a7 7 0 0 0-7-7zm0 9.5A2.5 2.5 0 1 1 8 4.5a2.5 2.5 0 0 1 0 5z"/></svg>Location</h3>
  <p>12 Harbour Lane, Suite 4, Northbridge<br>Sydney NSW 2063</p>
</div>
<div class="contact-col col-phone">
  <h3><svg width="16" height="16" viewBox="0 0 24 24"><path fill="#0f4a80" d="M6.6 10.8a15 15 0 0 0 6.6 6.6l2.2-2.2c.3-.3.7-.4 1-.2 1.1.4 2.3.6 3.6.6.6 0 1 .4 1 1V20c0 .6-.4 1-1 1A17 17 0 0 1 3 4c0-.6.4-1 1-1h3.5c.6 0 1 .4 1 1 0 1.3.2 2.5.6 3.6.1.3 0 .7-.2 1z"/></svg>Phone</h3>
  <p>+123 555 0190</p>
</div>
<div class="contact-col col-email">
  <h3><svg width="18" height="13" viewBox="0 0 20 14"><rect width="20" height="14" fill="#0f4a80"/><path d="M0 0 L10 8 L20 0" fill="none" stroke="#f1eff0" stroke-width="1.6"/></svg>Email</h3>
  <p>info@restwellclinic.com</p>
</div>
<div class="contact-col col-follow">
  <h3><svg width="20" height="16" viewBox="0 0 20 16"><path fill="#0f4a80" d="M1 5h4l7-4v14l-7-4H1z M4 11h3l1 5H5z"/><path d="M14 5l3-2M14 8h4M14 11l3 2" stroke="#0f4a80" stroke-width="1.4"/></svg>Follow Us</h3>
  <div class="social"><span></span><span></span><span></span><span></span></div>
</div>

<div class="footer-brand">Restwell</div>
<div class="footer-rule"></div>
<p class="copyright">Copyright © 2017 Restwell Australia. All Rights Reserved.</p>
<div class="bottom-line"></div>
</body>
</html>
```